Start up Dialysis Clinic needs its first website - Velmora Health

Create a visually appealing and user-friendly website for Velmora Health, a dialysis clinic located in Mt. Irvine, Tobago. The website should effectively communicate our services to local, regional, and international patients, providing essential information and fostering trust and engagement..
Key Goals:

1. Informative: Provide comprehensive information about our services, facility, and team.
2. User-Friendly: Ensure the website is easy to navigate, with a clear structure and accessible content.
3. Engaging: Create a visually appealing design that reflects the professionalism and care of Velmora Health.
4. Responsive: Ensure the website is fully responsive and performs well on all devices, including desktops, tablets, and smartphones.
5. Trust-Building: Include testimonials, credentials, and patient resources to build trust with potential patients.
Scope of Work:

1. Home Page: An inviting and informative landing page that provides an overview of our clinic, mission, and services. Include a call to action for more information and contact details.
2. About Us: A detailed page about Velmora Health, including our mission, vision, team, and facility tour.
3. Services: A comprehensive page describing the dialysis services we offer, including Hemodialysis, Peritoneal Dialysis, and Home Hemodialysis.
4. Patient Information: A resourceful section with guides for new patients, FAQs, insurance and billing information, and downloadable forms.
5. Resources: Educational content about kidney health, dialysis options, diet and nutrition tips, and support groups.
6. Contact Us: A contact page with our address, phone number, email, office hours, a contact form, and a map.

```html
<!DOCTYPE html>
<html lang="en">
<head>
<meta charset="utf-8">
<title>Velmora Health — Dialysis Clinic</title>
<link href="https://fonts.googleapis.com/css2?family=Open+Sans:wght@400;600;700;800&family=Arimo:wght@400;700&family=Tinos:wght@400&display=swap" rel="stylesheet">
<style>
:root{
  --navy:#182766;
  --navy-deep:#0f1d55;
  --blue:#3b6fb6;
  --green:#4f8f23;
  --green-dark:#3f7a1a;
  --ink:#1c2340;
  --text:#6b7180;
  --light:#f2f2f2;
  --pale:#f4f7fc;
  --footer:#0b1024;
  --white:#ffffff;
}
*{box-sizing:border-box;margin:0;padding:0}
html,body{width:1200px;height:4298px;overflow:hidden}
body{position:relative;font-family:"Open Sans",sans-serif;color:var(--ink);background:var(--white)}
.abs{position:absolute}
svg{display:block}

/* header */
.topbar{left:0;top:0;width:1200px;height:145px;background:var(--pale)}
.brand{left:100px;top:20px;width:140px;text-align:center}
.brand-mark{width:52px;height:52px;margin:0 auto 8px;background:var(--blue);border-radius:4px}
.brand-name{font-weight:700;font-size:23px;color:var(--blue);letter-spacing:.5px;line-height:1.1}
.contact-item{top:36px;display:flex;align-items:center;gap:12px;font-family:"Arimo",sans-serif;font-size:12.5px;color:#444;line-height:1.5}
.diamond{width:30px;height:30px;border:1px solid #c8d6be;transform:rotate(45deg);display:flex;align-items:center;justify-content:center;background:#fff}
.diamond svg{transform:rotate(-45deg)}
.navbar{left:243px;top:110px;width:882px;height:52px;background:#fff;border-radius:26px 0 0 26px;box-shadow:0 2px 6px rgba(0,0,0,.08)}
.navbar a{position:absolute;top:17px;font-family:"Arimo",sans-serif;font-size:13.5px;color:#333;text-decoration:none}
.btn-appoint{left:967px;top:113px;width:156px;height:47px;border-radius:24px;background:var(--green);color:#fff;font-family:"Arimo",sans-serif;font-size:14px;display:flex;align-items:center;justify-content:center;box-shadow:0 2px 6px rgba(0,0,0,.2)}

/* hero */
.hero-photo{left:0;top:145px;width:1200px;height:905px;background:linear-gradient(90deg,#1b2f74 0%,#2b4687 35%,#6e84a8 60%,#b7c3cf 80%,#d9dee2 100%)}
.hero-panel{left:90px;top:345px;width:530px;height:253px;background:rgba(20,35,90,.55)}
.hero-panel .bar{position:absolute;left:0;top:40px;width:5px;height:82px;background:var(--green)}
.hero-title{position:absolute;left:29px;top:35px;font-size:36px;font-weight:700;color:#fff;line-height:50px;letter-spacing:.5px}
.hero-text{position:absolute;left:29px;top:145px;width:480px;font-size:14px;color:#fff;line-height:29px}
.btn-demo{left:118px;top:567px;width:198px;height:45px;background:var(--green);color:#fff;font-weight:700;font-size:14px;display:flex;align-items:center;justify-content:center}

/* about */
.about-photo{left:0;top:1015px;width:455px;height:417px;border-radius:0 0 0 0;overflow:hidden}
.about-logo{left:363px;top:1053px;width:117px;height:117px;border-radius:50%;background:#e8eef5;display:flex;align-items:center;justify-content:center}
.about-logo span{width:56px;height:56px;background:var(--blue);border-radius:4px}
.eyebrow{font-size:12.5px;color:var(--green);font-weight:600;text-decoration:underline;text-underline-offset:4px}
.section-title{font-weight:700;color:var(--navy);letter-spacing:.5px}
.section-title em{font-style:normal;color:var(--blue)}
.about-title{left:604px;top:1022px;font-size:36px;line-height:47px}
.about-sub{left:604px;top:1142px;font-size:19px;color:var(--navy);font-weight:600}
.about-copy{left:604px;top:1183px;width:455px;font-size:12px;color:var(--text);line-height:19.5px}
.about-copy p+p{margin-top:11px}
.btn-contact{left:604px;top:1315px;width:137px;height:39px;background:var(--green);color:#fff;font-weight:600;font-size:14px;display:flex;align-items:center;justify-content:center;gap:14px}

/* services */
.services{left:0;top:1432px;width:1200px;height:663px;background:var(--light)}
.center{left:0;width:1200px;text-align:center}
.service-img{width:305px;height:282px;border-radius:4px}
.service-card{width:238px;height:142px;background:#fff;border-radius:4px;box-shadow:0 3px 10px rgba(0,0,0,.08);padding:35px 21px 0}
.service-card h3{font-size:16px;font-weight:700;color:var(--ink);margin-bottom:10px}
.service-card p{font-size:12.5px;color:var(--text);line-height:21px}
.icon-circle{width:60px;height:60px;border-radius:50%;background:var(--green);border:3px solid #fff;display:flex;align-items:center;justify-content:center}

/* why */
.why-photo{left:0;top:2095px;width:1200px;height:575px;background:linear-gradient(90deg,#d8dbdc 0%,#c9ccce 30%,#8d96a6 50%,#23346f 68%,#132163 100%)}
.why-title{left:620px;top:2170px;font-size:36px;font-weight:700;color:#fff;line-height:46px;letter-spacing:.5px}
.feature{left:625px;width:443px;height:105px;background:rgba(45,62,120,.75);border-left:4px solid var(--green);display:flex;align-items:center;padding-left:28px;gap:30px}
.feature.alt{border-left-color:#dcdcdc}
.feature h4{font-size:15px;color:#fff;font-weight:700;margin-bottom:4px}
.feature p{font-size:12.5px;color:#e2e6f0;line-height:20px;width:320px}

/* testimonials */
.testimonials{left:0;top:2670px;width:1200px;height:610px;background:var(--pale)}
.quote{width:305px;height:173px;background:#fff;padding:28px 22px;font-size:15px;line-height:23px;color:var(--ink);box-shadow:0 2px 8px rgba(0,0,0,.05)}
.quote.active{background:var(--green);color:#fff}
.quote-tail{width:0;height:0;border-top:18px solid var(--green);border-right:18px solid transparent}
.avatar{width:54px;height:54px;border-radius:50%;background:linear-gradient(135deg,#c7ced8,#8a95a6);border:3px solid #fff;box-shadow:0 1px 4px rgba(0,0,0,.15)}
.who b{display:block;font-size:14px;color:var(--ink)}
.who span{font-size:12px;color:#9aa0aa}
.dot{top:3200px;height:9px;border-radius:5px;background:var(--green)}

/* contact */
.touch-title{font-family:"Tinos",serif;font-size:46px;color:#222}
.touch-title em{font-style:normal;color:var(--blue)}
.contact-box{left:147px;top:3430px;width:908px;height:290px;background:#fff;box-shadow:0 3px 12px rgba(0,0,0,.1)}
.address-panel{position:absolute;left:0;top:0;width:303px;height:290px;background:var(--light)}
.address-panel h3{position:absolute;left:33px;top:25px;font-family:"Tinos",serif;font-weight:400;font-size:34px;color:#333}
.addr-row{position:absolute;left:32px;display:flex;gap:10px;font-size:13.5px;color:#222;line-height:20px}
.field{position:absolute;font-size:13px;color:#333;border-bottom:1px solid #aaa;padding-bottom:8px}
.btn-enquiry{position:absolute;left:325px;top:215px;width:186px;height:37px;border-radius:19px;background:var(--green);color:#fff;font-family:"Tinos",serif;font-size:14px;display:flex;align-items:center;justify-content:center;gap:10px}

/* footer */
.footer{left:0;top:3760px;width:1200px;height:538px;background:var(--footer)}
.foot-pill{width:272px;height:52px;border-top:6px solid #1e2538;border-bottom:6px solid #1e2538;display:flex;align-items:center;justify-content:center;gap:10px;color:#fff}
.social{top:4157px;left:538px;display:flex;gap:9px}
.social span{width:19px;height:19px;border-radius:50%;background:#fff}
.foot-nav{top:4216px;left:0;width:1200px;display:flex;justify-content:center;gap:0}
.foot-nav a{color:#fff;font-size:12.5px;text-decoration:none;font-weight:600;margin:0 19px}
</style>
</head>
<body>

<!-- header -->
<div class="abs topbar"></div>
<div class="abs brand"><div class="brand-mark"></div><div class="brand-name">Velmora Health</div></div>

<div class="abs contact-item" style="left:418px">
  <div class="diamond"><svg width="12" height="14" viewBox="0 0 12 14"><path d="M6 0a5 5 0 0 0-5 5c0 4 5 9 5 9s5-5 5-9a5 5 0 0 0-5-5z" fill="#4f8f23"/><circle cx="6" cy="5" r="1.8" fill="#fff"/></svg></div>
  <div>Email Address<br>care@velmoramail.com</div>
</div>
<div class="abs contact-item" style="left:663px">
  <div class="diamond"><svg width="12" height="14" viewBox="0 0 12 14"><path d="M6 0a5 5 0 0 0-5 5c0 4 5 9 5 9s5-5 5-9a5 5 0 0 0-5-5z" fill="#4f8f23"/><circle cx="6" cy="5" r="1.8" fill="#fff"/></svg></div>
  <div>Email Address<br>care@velmoramail.com</div>
</div>
<div class="abs contact-item" style="left:909px">
  <div class="diamond"><svg width="12" height="14" viewBox="0 0 12 14"><path d="M6 0a5 5 0 0 0-5 5c0 4 5 9 5 9s5-5 5-9a5 5 0 0 0-5-5z" fill="#4f8f23"/><circle cx="6" cy="5" r="1.8" fill="#fff"/></svg></div>
  <div>Email Address<br>care@velmoramail.com</div>
</div>

<!-- hero -->
<div class="abs hero-photo" role="img" aria-label="Doctor and nurse in masks reviewing a chart in a hospital corridor"></div>
<svg class="abs" style="left:0;top:790px" width="1200" height="270" viewBox="0 0 1200 270">
  <path d="M0 40 Q330 -10 640 35 Q950 80 1200 260 L1200 270 L0 270Z" fill="#fff"/>
  <path d="M640 35 Q950 80 1200 180 L1200 260 Q960 80 640 35Z" fill="#4f8f23"/>
</svg>

<nav class="abs navbar">
  <a style="left:68px">Home</a>
  <a style="left:158px">About Us</a>
  <a style="left:245px">Services</a>
  <a style="left:327px">Our Team</a>
  <a style="left:427px">Projects</a>
</nav>
<div class="abs btn-appoint">Appointment</div>

<div class="abs hero-panel">
  <div class="bar"></div>
  <h1 class="hero-title">Empower your Body,<br>Empower your Life.</h1>
  <p class="hero-text">It is a long and established fact that a reader will be distracted by the readable content of a page when looking.</p>
</div>
<div class="abs btn-demo">REQUEST A DEMO</div>

<!-- about -->
<svg class="abs" style="left:0;top:1013px" width="460" height="420" viewBox="0 0 460 420">
  <path d="M0 60 Q100 0 230 0 A225 225 0 0 1 400 420 L0 420Z" fill="#4f8f23"/>
</svg>
<div class="abs" style="left:0;top:1015px;width:445px;height:417px;background:linear-gradient(135deg,#9fb3c8,#d8dde2 55%,#7f92ab);clip-path:path('M0 60 Q100 2 225 2 A221 221 0 0 1 395 417 L0 417Z')" role="img" aria-label="Smiling doctor in a white coat holding a clipboard"></div>
<div class="abs about-logo"><span></span></div>

<div class="abs eyebrow" style="left:604px;top:992px">WHO WE ARE</div>
<h2 class="abs section-title about-title">Your Partner in <em>Kidney<br>Wellness</em></h2>
<div class="abs about-sub">Transform your body, transform your life.</div>
<div class="abs about-copy">
  <p>Lorem ipsum dolor sit amet, consectetur adipiscing elit, sed do eiusmod temp or incididunt ut labore et dolore magna aliqua. Ut enim ad minim veniam, quis laboris nisi ut aliquip ex ea commodo consequat.</p>
  <p>Lorem ipsum dolor sit amet, consectetur adipiscing elit, sed do eiusmod temp or incididunt ut labore et dolore magna aliqua.</p>
</div>
<div class="abs btn-contact">Contact us <svg width="16" height="12" viewBox="0 0 16 12"><path d="M1 6h13M9 1l5 5-5 5" stroke="#fff" stroke-width="1.5" fill="none"/></svg></div>

<!-- services -->
<div class="abs services"></div>
<div class="abs center eyebrow" style="top:1522px">OUR SERVICES</div>
<h2 class="abs center section-title" style="top:1558px;font-size:40px"><em>Services</em> We Provide</h2>

<div class="abs service-img" style="left:118px;top:1653px;background:linear-gradient(135deg,#c9d3dc,#9aa8b8 60%,#b36060)" role="img" aria-label="Patient receiving hemodialysis"></div>
<div class="abs service-img" style="left:446px;top:1653px;background:linear-gradient(135deg,#1e2d4e,#7b8ca5 50%,#e6eaee)" role="img" aria-label="Doctor examining a kidney model with a magnifier"></div>
<div class="abs service-img" style="left:774px;top:1653px;background:linear-gradient(135deg,#4b6a9a,#cfd6e0 55%,#8a9bb5)" role="img" aria-label="Arm connected to home hemodialysis lines"></div>

<div class="abs service-card" style="left:185px;top:1880px"><h3>Hemodialysis</h3><p>Lorem ipsum dolor sit amet, co nsectetur adipiscing elit, s</p></div>
<div class="abs service-card" style="left:513px;top:1880px"><h3>Peritoneal Dialysis</h3><p>Lorem ipsum dolor sit amet, co nsectetur adipiscing elit, s</p></div>
<div class="abs service-card" style="left:841px;top:1880px"><h3>Home Hemodialysis</h3><p>Lorem ipsum dolor sit amet, co nsectetur adipiscing elit, s</p></div>

<div class="abs icon-circle" style="left:155px;top:1850px"><svg width="26" height="26" viewBox="0 0 26 26" fill="none" stroke="#fff" stroke-width="1.6"><circle cx="13" cy="6" r="3.5"/><path d="M4 23h18M8 23l4-9 6 5"/></svg></div>
<div class="abs icon-circle" style="left:483px;top:1850px"><svg width="26" height="26" viewBox="0 0 26 26" fill="none" stroke="#fff" stroke-width="1.6"><circle cx="13" cy="6" r="3.5"/><path d="M4 23h18M8 23l4-9 6 5"/></svg></div>
<div class="abs icon-circle" style="left:811px;top:1850px"><svg width="26" height="26" viewBox="0 0 26 26" fill="none" stroke="#fff" stroke-width="1.6"><circle cx="13" cy="6" r="3.5"/><path d="M4 23h18M8 23l4-9 6 5"/></svg></div>

<!-- why choose -->
<div class="abs why-photo" role="img" aria-label="Overhead view of a doctor and nurse walking through a bright corridor"></div>
<div class="abs eyebrow" style="left:620px;top:2144px;font-size:11px">WHY CHOOSE US</div>
<h2 class="abs why-title">Healthy today,<br>happier tomorrow.</h2>

<div class="abs feature" style="top:2285px">
  <svg width="36" height="36" viewBox="0 0 36 36" fill="none" stroke="#fff" stroke-width="1.6"><circle cx="18" cy="8" r="5"/><path d="M5 32h26M11 32l6-13 9 7"/></svg>
  <div><h4>CLIENT-CENTRIC</h4><p>Lorem ipsum dolor sit amet, consectetur adipiscing elit, sed do eiusmod tempor incidid</p></div>
</div>
<div class="abs feature alt" style="top:2398px">
  <svg width="36" height="36" viewBox="0 0 36 36" fill="none" stroke="#fff" stroke-width="1.6"><path d="M18 3l4 7 8 1-5 6 2 8-9-3-9 3 2-8-5-6 8-1z"/><circle cx="18" cy="17" r="4"/></svg>
  <div><h4>PROFESSIONALISM</h4><p>Lorem ipsum dolor sit amet, consectetur adipiscing elit, sed do eiusmod tempor incidid</p></div>
</div>
<div class="abs feature alt" style="top:2510px">
  <svg width="36" height="36" viewBox="0 0 36 36" fill="none" stroke="#fff" stroke-width="1.6"><path d="M5 28a14 14 0 1 1 26 0"/><path d="M18 20l6-7"/><circle cx="18" cy="21" r="2"/></svg>
  <div><h4>EXPERIENCED EXPERTS</h4><p>Lorem ipsum dolor sit amet, consectetur adipiscing elit, sed do eiusmod tempor incidid</p></div>
</div>

<!-- testimonials -->
<div class="abs testimonials"></div>
<div class="abs center eyebrow" style="top:2764px">TESTIMONIALS</div>
<h2 class="abs center section-title" style="top:2798px;font-size:40px;color:var(--navy)">What <em>Clients</em> are Saying</h2>

<div class="abs quote" style="left:118px;top:2897px">Lorem ipsum dolor sit amet, consectetur adipiscing elit, sed d o eiusmod tempor incididunt ut lab ore et dolore magna aliqua. Ut enim ad min</div>
<div class="abs quote active" style="left:446px;top:2897px">Lorem ipsum dolor sit amet, consectetur adipiscing elit, sed d o eiusmod tempor incididunt ut lab ore et dolore magna aliqua. Ut enim ad min</div>
<div class="abs quote" style="left:776px;top:2897px">Lorem ipsum dolor sit amet, consectetur adipiscing elit, sed d o eiusmod tempor incididunt ut lab ore et dolore magna aliqua. Ut enim ad min</div>
<div class="abs quote-tail" style="left:118px;top:3070px"></div>
<div class="abs quote-tail" style="left:446px;top:3070px"></div>
<div class="abs quote-tail" style="left:776px;top:3070px"></div>

<div class="abs avatar" style="left:137px;top:3097px" role="img" aria-label="Client portrait"></div>
<div class="abs who" style="left:210px;top:3097px"><b>Dana Reyes</b><span>Engineer</span></div>
<div class="abs avatar" style="left:465px;top:3097px" role="img" aria-label="Client portrait"></div>
<div class="abs who" style="left:538px;top:3097px"><b>Dana Reyes</b><span>Engineer</span></div>
<div class="abs avatar" style="left:795px;top:3097px" role="img" aria-label="Client portrait"></div>
<div class="abs who" style="left:868px;top:3097px"><b>Dana Reyes</b><span>Engineer</span></div>

<div class="abs dot" style="left:570px;width:22px"></div>
<div class="abs dot" style="left:597px;width:9px"></div>
<div class="abs dot" style="left:611px;width:9px"></div>
<div class="abs dot" style="left:625px;width:9px"></div>

<!-- contact -->
<h2 class="abs center touch-title" style="top:3325px">Get In <em>Touch</em></h2>

<svg class="abs" style="left:0;top:3640px" width="1200" height="130" viewBox="0 0 1200 130">
  <path d="M0 20 Q200 110 730 120 Q1000 122 1200 100 L1200 130 L0 130Z" fill="#0b1024"/>
  <path d="M0 0 Q180 100 730 120 Q260 120 0 60Z" fill="#4f8f23"/>
</svg>

<div class="abs contact-box">
  <div class="address-panel">
    <h3>Address</h3>
    <div class="addr-row" style="top:95px">
      <svg width="20" height="20" viewBox="0 0 20 20" fill="none" stroke="#4f8f23" stroke-width="1.4"><circle cx="10" cy="5" r="3"/><path d="M2 18h16M5 18l4-8 5 4"/></svg>
      <div>Company Name<br>Place 2134 Ave<br>City, Country</div>
    </div>
    <div class="addr-row" style="top:170px;font-weight:700;font-size:12.5px">
      <svg width="20" height="20" viewBox="0 0 20 20" fill="none" stroke="#4f8f23" stroke-width="1.4"><path d="M4 2h4l2 5-2.5 1.5a10 10 0 0 0 4 4L13 10l5 2v4a2 2 0 0 1-2 2A15 15 0 0 1 2 4a2 2 0 0 1 2-2z"/></svg>
      <div>868-555-0190 Or 868-555-0117</div>
    </div>
    <div class="addr-row" style="top:210px;font-size:13px">
      <svg width="20" height="20" viewBox="0 0 20 20" fill="none" stroke="#4f8f23" stroke-width="1.4"><rect x="3" y="2" width="14" height="16" rx="1"/><circle cx="10" cy="8" r="2.5"/><path d="M6 15c1-3 7-3 8 0"/></svg>
      <div>info@velmoramail.com</div>
    </div>
  </div>
  <div class="field" style="left:323px;top:48px;width:266px">Name:</div>
  <div class="field" style="left:625px;top:48px;width:266px;height:30px"></div>
  <div class="field" style="left:323px;top:94px;width:266px">Phone:</div>
  <div class="field" style="left:625px;top:94px;width:266px;height:30px"></div>
  <div class="field" style="left:323px;top:137px;width:563px;height:58px">Details:</div>
  <div class="btn-enquiry">QUICK ENQUIRY <svg width="14" height="12" viewBox="0 0 16 12"><path d="M1 6h13M9 1l5 5-5 5" stroke="#fff" stroke-width="1.5" fill="none"/></svg></div>
</div>

<!-- footer -->
<div class="abs footer"></div>
<div class="abs" style="left:450px;top:3990px;width:300px;text-align:center">
  <div style="width:64px;height:64px;margin:0 auto 12px;background:var(--blue);border-radius:4px"></div>
  <div style="font-weight:700;font-size:29px;color:var(--blue);line-height:1.1">Velmora Health</div>
  <div style="font-size:12px;color:var(--green);margin-top:12px">info@velmoramail.com</div>
</div>
<div class="abs foot-pill" style="left:175px;top:4059px;font-size:12px;line-height:15px">
  <svg width="14" height="18" viewBox="0 0 12 14"><path d="M6 0a5 5 0 0 0-5 5c0 4 5 9 5 9s5-5 5-9a5 5 0 0 0-5-5z" fill="#4f8f23"/><circle cx="6" cy="5" r="1.8" fill="#0b1024"/></svg>
  <div>12 SHORE ROAD<br>TOBAGO</div>
</div>
<div class="abs foot-pill" style="left:760px;top:4059px;font-size:21px">
  <svg width="14" height="18" viewBox="0 0 12 14"><path d="M6 0a5 5 0 0 0-5 5c0 4 5 9 5 9s5-5 5-9a5 5 0 0 0-5-5z" fill="#4f8f23"/><circle cx="6" cy="5" r="1.8" fill="#0b1024"/></svg>
  <div>868 555 0142</div>
</div>
<div class="abs social"><span></span><span></span><span></span><span></span><span></span></div>
<nav class="abs foot-nav">
  <a>HOME</a><a>SERVICES</a><a>ABOUT US</a><a>PROJECTS</a><a>TESTIMONIALS</a><a>FAQ</a><a>CONTACT US</a>
</nav>

</body>
</html>
```